Energy Solution company Needs a PowerPoint Design

We need a PowerPoint design for new energy solution company based in Houston. major markets / clients in Africa called ''RV Mavrek Solutions'' . We provider variety of professional services, systems ,and project management solutions to Oil & Gas, Power , Telecommunication , ICT, Airlines & Transportation , Social & Public Sector and Utilities & Alternative Energy industries. We would like to see a simple PowerPoint designs but statement. The final design should communicate engineering Integrity, quality and safety. See attached file with template and company logo. please use logo color combination.

Target Market(s)

Oil & Gas, Power , Telecommunication , ICT, Airlines & Transportation , Social & Public Sector and Utilities & Alternative Energy industries.

Industry/Entity Type

It Company

Font styles to use
Other font styles liked:
• Century Gothic

Colors
ffc214
aaaaaa
0355a3

Requirements
Must have
• engineering details oriented simple looks. SEE ATTACHED PPT WITH COMPANY LOGO AND TEMPLATE. PLEASE ATTACHED LOGO COLOR COMBINATION.]
• We will like to see 5 text boxes with different images across the middle of the cover page, this images will be from below Industries:
• • Oil and Gas
• • Power
• • Information Technology
• • Manufacturing Industry
• • Higher Education Industry
• Please don't include the Industries name as list above, We just want the images.
Nice to have
• • Oil and Gas
• • Power

```html
<!DOCTYPE html>
<html lang="en">
<head>
<meta charset="utf-8">
<title>Main Process</title>
<link href="https://fonts.googleapis.com/css2?family=Arimo:wght@400;700&display=swap" rel="stylesheet">
<style>
  :root {
    --slide-bg: #ffffff;
    --title-ink: #4a4a4a;
    --step-fill: #f67b1c;
    --step-edge: #d9620c;
    --detail-fill: #0b2c5f;
    --detail-edge: #e07a2a;
    --connector: #333333;
    --arrow: #4d4d4d;
    --rule: #1f3f73;
    --footer-ink: #555555;
    --on-dark: #ffffff;
  }
  * { margin: 0; padding: 0; box-sizing: border-box; }
  html, body { width: 1200px; height: 675px; overflow: hidden; background: var(--slide-bg); }
  .slide {
    position: relative;
    width: 1200px;
    height: 675px;
    background: var(--slide-bg);
    font-family: "Arimo", Arial, sans-serif;
  }
  .slide-title {
    position: absolute;
    left: 0; right: 0; top: 16px;
    text-align: center;
    font-size: 44px;
    font-weight: 700;
    color: var(--title-ink);
    letter-spacing: 0.5px;
  }
  .box {
    position: absolute;
    display: flex;
    align-items: center;
    justify-content: center;
    text-align: center;
    color: var(--on-dark);
    font-size: 21px;
    line-height: 1.25;
    border-radius: 9px;
    padding: 0 14px;
  }
  .step {
    left: 82px; width: 351px; height: 78px;
    background: var(--step-fill);
    border: 1px solid var(--step-edge);
  }
  .detail {
    left: 674px; width: 450px; height: 77px;
    background: var(--detail-fill);
    border: 1.5px solid var(--detail-edge);
  }
  .connector {
    position: absolute;
    left: 515px; width: 127px; height: 1.5px;
    background: var(--connector);
  }
  .flow-arrow { position: absolute; left: 230px; width: 26px; height: 20px; }
  .footer-rule {
    position: absolute;
    left: 82px; width: 1045px; top: 626px; height: 1px;
    background: var(--rule);
  }
  .footer-text {
    position: absolute;
    font-size: 11px;
    color: var(--footer-ink);
  }
</style>
</head>
<body>
<div class="slide">
  <h1 class="slide-title">Main Process</h1>

  <svg class="flow-arrow" style="top:69px" viewBox="0 0 26 20"><path d="M8 0h10v9h8L13 20 0 9h8z" fill="var(--arrow)"/></svg>
  <div class="box step" style="top:91px">Business Development</div>
  <div class="connector" style="top:140px"></div>
  <div class="box detail" style="top:103px">Markets Clients Products</div>

  <svg class="flow-arrow" style="top:184px" viewBox="0 0 26 20"><path d="M8 0h10v9h8L13 20 0 9h8z" fill="var(--arrow)"/></svg>
  <div class="box step" style="top:206px">Tender &amp; Contracts</div>
  <div class="connector" style="top:255px"></div>
  <div class="box detail" style="top:218px">Tender, Negotiations, Contract Review</div>

  <svg class="flow-arrow" style="top:292px" viewBox="0 0 26 20"><path d="M8 0h10v9h8L13 20 0 9h8z" fill="var(--arrow)"/></svg>
  <div class="box step" style="top:314px">HSE &amp; Risk<br>Management</div>
  <div class="connector" style="top:364px"></div>
  <div class="box detail" style="top:327px">Emergency Preparedness, SJA, Risk Analysis, Method Statement</div>

  <svg class="flow-arrow" style="top:403px" viewBox="0 0 26 20"><path d="M8 0h10v9h8L13 20 0 9h8z" fill="var(--arrow)"/></svg>
  <div class="box step" style="top:424px">Project Execution</div>
  <div class="connector" style="top:467px"></div>
  <div class="box detail" style="top:430px">Network Critical Path, Project Execution</div>

  <svg class="flow-arrow" style="top:508px" viewBox="0 0 26 20"><path d="M8 0h10v9h8L13 20 0 9h8z" fill="var(--arrow)"/></svg>
  <div class="box step" style="top:530px">Engineering</div>
  <div class="connector" style="top:575px"></div>
  <div class="box detail" style="top:537px">Design Basis, Design Control, Control Plan, Specifications</div>

  <div class="footer-rule"></div>
  <div class="footer-text" style="left:82px; top:634px">6-Jul-15</div>
  <div class="footer-text" style="left:584px; top:634px">Slide 3</div>
  <div class="footer-text" style="left:82px; top:653px">© 2015 RV Mavrek Solutions</div>
</div>
</body>
</html>
```